Dental Office Business Card

We need a business card for our pediatric dentistry office.
On one side the design needs to contain the following:
our logo (attached)
Vento Pediatric Grins
Soraya Kadbelani, DDS
Board Certified Pediatric Dentist
Tel: (555) 318-2747)
Fax: (555) 264-8031
Email: info@ventopediatricgrins.example
Web: www.ventopediatricgrins.example
Address: 41 Brindle Ave, Suite 208, Larkmoor, ZN 02099

On the other side of the card, the design needs to have an appointment reminder (date and time as well as day of the week) similar to the design attached (no need for appointment reason “For”)

```html
<!DOCTYPE html>
<html lang="en">
<head>
<meta charset="utf-8">
<title>Vento Pediatric Grins – Business Card</title>
<link href="https://fonts.googleapis.com/css2?family=Montserrat:wght@400;600;700&family=Cinzel:wght@600&family=Marcellus&display=swap" rel="stylesheet">
<style>
  :root {
    --backdrop: #1e1e1e;
    --card: #f3f3f2;
    --ink: #2b2b2b;
    --mint: #93cf9f;
    --charcoal: #2d2d2d;
    --rule: #555555;
    --box: #a9a9a9;
  }
  * { margin: 0; padding: 0; box-sizing: border-box; }
  html, body { width: 1200px; height: 1059px; overflow: hidden; }
  body {
    background: var(--backdrop);
    position: relative;
    font-family: "Montserrat", sans-serif;
    color: var(--ink);
  }
  .card {
    position: absolute;
    background: var(--card);
    border-radius: 22px;
    overflow: hidden;
  }
  .card-front { left: 257px; top: 89px; width: 687px; height: 390px; }
  .card-back  { left: 254px; top: 547px; width: 693px; height: 394px; }

  /* Front */
  .brand {
    position: absolute; left: 0; right: 0; top: 58px;
    display: flex; align-items: center; justify-content: center; gap: 16px;
  }
  .brand-dot {
    width: 52px; height: 52px; border-radius: 50%;
    background: var(--mint);
  }
  .brand-name {
    font-weight: 700; font-size: 34px; line-height: 1.08;
    color: var(--ink);
  }
  .dentist {
    position: absolute; right: 365px; top: 232px; text-align: right;
  }
  .dentist-name {
    font-weight: 600; font-size: 22px; color: var(--mint); white-space: nowrap;
  }
  .dentist-title {
    font-size: 14.5px; margin-top: 5px; white-space: nowrap;
  }
  .divider {
    position: absolute; left: 342px; top: 217px; width: 1px; height: 80px;
    background: var(--mint);
  }
  .contacts {
    position: absolute; left: 363px; top: 211px; list-style: none;
  }
  .contacts li {
    display: flex; align-items: center; gap: 9px;
    font-size: 15px; height: 22.6px; white-space: nowrap;
  }
  .contacts svg { width: 12px; height: 12px; flex: none; }
  .address {
    position: absolute; left: 0; right: 0; top: 329px;
    text-align: center; font-size: 15px;
  }
  .band { position: absolute; left: 0; bottom: 0; width: 100%; height: 12px; }

  /* Back */
  .reminder-head { position: absolute; left: 0; right: 0; top: 64px; text-align: center; }
  .reminder-title {
    font-family: "Cinzel", serif; font-weight: 600; font-size: 29px;
    letter-spacing: 3px; color: #151515;
  }
  .reminder-sub {
    font-weight: 600; font-size: 24px; color: var(--mint);
  }
  .field {
    position: absolute; left: 46px; display: flex; align-items: flex-end;
    font-weight: 600; font-size: 19px;
  }
  .field-date { top: 197px; width: 600px; }
  .field-time { top: 259px; width: 601px; }
  .field-line {
    flex: 1; border-bottom: 1px solid var(--rule); margin: 0 0 4px 10px;
  }
  .field-suffix { margin-left: 8px; }
  .days {
    position: absolute; left: 45px; width: 602px; top: 322px;
    display: flex; justify-content: space-between; list-style: none;
    font-family: "Marcellus", serif; font-size: 18px; letter-spacing: 2px;
  }
  .days li { display: flex; align-items: center; gap: 8px; }
  .days .check {
    width: 20px; height: 20px; border: 1px solid var(--box); background: #fafafa;
  }
</style>
</head>
<body>

<section class="card card-front" aria-label="Business card front">
  <div class="brand">
    <span class="brand-dot" aria-hidden="true"></span>
    <span class="brand-name">Vento<br>Pediatric Grins</span>
  </div>

  <div class="dentist">
    <p class="dentist-name">Soraya Kadbelani, DDS</p>
    <p class="dentist-title">Board Certified Pediatric Dentist</p>
  </div>

  <div class="divider"></div>

  <ul class="contacts">
    <li>
      <svg viewBox="0 0 24 24" fill="var(--mint)" aria-label="Phone"><path d="M6.6 10.8a15.1 15.1 0 0 0 6.6 6.6l2.2-2.2a1 1 0 0 1 1-.25 11.4 11.4 0 0 0 3.6.57 1 1 0 0 1 1 1V20a1 1 0 0 1-1 1A17 17 0 0 1 3 4a1 1 0 0 1 1-1h3.5a1 1 0 0 1 1 1c0 1.25.2 2.45.57 3.6a1 1 0 0 1-.25 1z"/></svg>
      (555) 318-2747)
    </li>
    <li>
      <svg viewBox="0 0 24 24" fill="var(--mint)" aria-label="Fax"><path d="M6 2h12v5H6zM4 8h16a2 2 0 0 1 2 2v7h-4v5H6v-5H2v-7a2 2 0 0 1 2-2zm4 8v4h8v-4z"/></svg>
      (555) 264-8031
    </li>
    <li>
      <svg viewBox="0 0 24 24" fill="var(--mint)" aria-label="Email"><path d="M2 5h20v14H2zm2 2v.5l8 5 8-5V7l-8 5z"/></svg>
      info@ventopediatricgrins.example
    </li>
    <li>
      <svg viewBox="0 0 24 24" fill="none" stroke="var(--mint)" stroke-width="2" aria-label="Website"><circle cx="12" cy="12" r="10"/><path d="M2 12h20M12 2c3 3 3 17 0 20M12 2c-3 3-3 17 0 20"/></svg>
      www.ventopediatricgrins.example
    </li>
  </ul>

  <p class="address">41 Brindle Ave, Suite 208, Larkmoor, ZN 02099</p>

  <svg class="band" viewBox="0 0 687 12" preserveAspectRatio="none" aria-hidden="true">
    <polygon points="0,0 355,0 338,12 0,12" fill="var(--mint)"/>
    <polygon points="359,0 687,0 687,12 342,12" fill="var(--charcoal)"/>
  </svg>
</section>

<section class="card card-back" aria-label="Appointment reminder side">
  <header class="reminder-head">
    <h1 class="reminder-title">APPOINTMENT</h1>
    <p class="reminder-sub">Reminder</p>
  </header>

  <div class="field field-date">
    <span>Date :</span><span class="field-line"></span>
  </div>
  <div class="field field-time">
    <span>Time :</span><span class="field-line"></span><span class="field-suffix">am/pm</span>
  </div>

  <ul class="days">
    <li><span class="check"></span>Mon</li>
    <li><span class="check"></span>Tue</li>
    <li><span class="check"></span>Wed</li>
    <li><span class="check"></span>Thu</li>
    <li><span class="check"></span>Fri</li>
    <li><span class="check"></span>Sat</li>
    <li><span class="check"></span>Sun</li>
  </ul>
</section>

</body>
</html>
```